Veltrano Strom GmbH webpage The online Business card of a master electrician

A clean, modern webpage on whitch i can show my clients what im capable of and where the future costumer can inform himself. I need a login page for costumers who are registred and an secound webpage where my stuff can login to report theyr labour.
I will post pictures before and after, put on some commercial and crossellimg informations.
The costumer should find my insta as well my twitter or snapchat accounts.

Update:
Our Services are, Installations, Renovations, Home Automation, CCTV, Telefon / VOIP, Networking / Network-Cabeling, Electrical Supervisioning

Target Market(s)

Private and business costumers

Industry/Entity Type

Electric Company

Number of Pages Required

5+ page

Font styles to use
Sans Serif
Other font styles liked:
• Zurich,

Colors

Designer to choose colors to be used in the design.

Requirements
Must have
• A Page Hero
• A Costumer and staff login page (2separate pages)
• Contact form
• Responsive form
• Instagram enbedding account veltrano_strom
Nice to have
• A Blog

```html
<!DOCTYPE html>
<html lang="en">
<head>
<meta charset="utf-8">
<title>Veltrano Strom GmbH</title>
<link rel="stylesheet" href="https://fonts.googleapis.com/css2?family=Open+Sans:wght@400;600;700&family=Arimo:wght@400;700&display=swap">
<style>
:root{
  --black:#000;
  --blue:#0047b3;
  --blue-bright:#0a98e0;
  --grey:#878787;
  --grey-dark:#6e6e6e;
  --white:#fff;
  --text:#6b6b6b;
  --heading-blue:#0b4cb0;
}
*{box-sizing:border-box;margin:0;padding:0}
html,body{width:804px;height:1200px;overflow:hidden;background:var(--white)}
body{position:relative;font-family:"Arimo",Arial,sans-serif}
.abs{position:absolute}
.site-header{left:0;top:0;width:804px;height:98px;background:var(--black);display:flex;align-items:center;justify-content:center;gap:10px}
.brand-mark{width:22px;height:22px;background:var(--blue-bright)}
.brand-name{font-family:"Open Sans",sans-serif;font-weight:700;font-size:30px;color:var(--blue-bright);letter-spacing:1px}
.main-nav{left:0;top:98px;width:804px;height:28px;background:var(--grey);display:flex;align-items:center;padding-left:82px;gap:24px;font-family:"Open Sans",sans-serif;font-size:10px;color:var(--white)}
.main-nav .active{color:var(--blue);font-weight:600}
.hero{left:0;top:126px;width:574px;height:240px;background:linear-gradient(120deg,#3a3128,#6d5a43 45%,#2a2520 80%)}
.hero-shade{left:0;top:126px;width:574px;height:240px;background:linear-gradient(90deg,rgba(0,0,0,.1),rgba(0,0,0,.45))}
.hero-side{left:755px;top:126px;width:49px;height:240px;background:var(--black)}
.hero-title{left:82px;top:186px;font-family:"Open Sans",sans-serif;font-weight:700;font-size:30px;line-height:38px;color:var(--white)}
.hero-text{left:83px;top:264px;width:305px;font-size:7px;line-height:8.8px;color:var(--white)}
.hero-arrow{top:228px;font-family:"Open Sans",sans-serif;font-size:26px;color:#bbb}
.register{left:574px;top:98px;width:181px;height:268px;background:var(--blue);padding:5px 6px}
.register h2{font-family:"Open Sans",sans-serif;font-weight:700;font-size:16px;color:var(--white);text-align:center;margin-bottom:8px}
.field{height:32px;background:var(--white);margin:0 0 17px 6px;width:168px;display:flex;align-items:center;gap:4px;padding-left:6px;font-family:"Open Sans",sans-serif;font-size:14px;color:#777}
.submit{margin:-4px 0 0 32px;width:118px;height:26px;background:var(--grey);border:1px solid #aaa;color:var(--white);font-family:"Open Sans",sans-serif;font-size:14px;display:flex;align-items:center;justify-content:center}
.grow{left:0;top:366px;width:804px;height:168px;background:var(--grey);color:var(--white);text-align:center}
.grow h2{margin-top:9px;font-family:"Open Sans",sans-serif;font-weight:700;font-size:16px}
.grow .intro{width:590px;margin:3px auto 0;font-size:7.5px;line-height:10px}
.feature{position:absolute;top:56px;width:120px;text-align:center}
.feature h3{font-weight:400;font-size:9.5px;margin:6px 0 9px}
.feature p{font-size:7px;line-height:10px;padding:0 6px}
.services-photo{left:49px;top:540px;width:353px;height:198px;background:linear-gradient(180deg,#7a8ea8,#c9a88a 45%,#3b4a66 60%,#6e85a8)}
.services-title{left:418px;top:542px;font-family:"Open Sans",sans-serif;font-weight:700;font-size:16px;color:var(--heading-blue)}
.services-text{left:418px;top:571px;width:312px;font-family:"Open Sans",sans-serif;font-size:8.8px;line-height:11.2px;color:var(--text);text-align:justify}
.team{left:0;top:747px;width:804px;height:131px;background:var(--blue);color:var(--white)}
.team h2{text-align:center;font-family:"Open Sans",sans-serif;font-weight:700;font-size:16px;margin-top:6px}
.team p{width:714px;margin:3px 0 0 54px;font-size:7px;line-height:8.8px;font-weight:700}
.team-button{left:310px;top:826px;width:184px;height:42px;background:var(--blue-bright);color:var(--white);font-family:"Open Sans",sans-serif;font-size:12px;display:flex;align-items:center;justify-content:center;border-radius:2px}
.blog-title{left:0;top:880px;width:804px;text-align:center;font-family:"Open Sans",sans-serif;font-weight:700;font-size:16px;color:var(--heading-blue)}
.post{top:902px;width:201px}
.post-thumb{height:93px;background:#e2e2e2;display:flex;align-items:center;justify-content:center}
.post h3{text-align:center;font-weight:400;font-size:15px;margin:4px 0 2px;color:#000}
.post p{font-size:8px;line-height:11px;color:#222;height:61px;overflow:hidden}
.post a{display:block;text-align:right;font-size:8px;color:#2a6dd1;margin-top:8px;padding-right:3px}
.site-footer{left:0;top:1118px;width:804px;height:82px;background:var(--black);color:var(--white);text-align:center}
.footer-links{margin-top:15px;font-size:15px}
.socials{display:flex;justify-content:center;gap:9px;margin-top:10px}
.social{width:29px;height:29px;border-radius:7px}
</style>
</head>
<body>
<header class="abs site-header">
  <span class="brand-mark"></span><span class="brand-name">VELTRANO STROM</span>
</header>
<nav class="abs main-nav">
  <span class="active">HOME</span><span>ABOUT</span><span>SERVICES</span><span>VIDEOS</span><span>EVENTS</span><span>OUR TEAM</span><span>BLOG</span><span style="margin-left:4px">CONTACT US</span>
</nav>

<div class="abs hero" role="img" aria-label="Photo of a warmly lit restaurant interior with tables and pendant lights"></div>
<div class="abs hero-shade"></div>
<div class="abs hero-side"></div>
<span class="abs hero-arrow" style="left:50px">‹</span>
<span class="abs hero-arrow" style="left:550px">›</span>
<h1 class="abs hero-title">LEARN MORE<br>VELTRANO STROM</h1>
<p class="abs hero-text">Lorem ipsum dolor sit amet, consectetur adipiscing elit. Nulla quam velit, vulputate eu pharetra nec, mattis ac neque. Duis vulputate commodo lectus, ac blandit elit tincidunt id. Sed rhoncus, tortor sed eleifend tristique, tortor mauris molestie elit, et lacinia ipsum quam nec dui. Quisque nec mauris sit amet elit iaculis pretium sit amet quis magna. Aenean velit odio, elementum in tempus ut, vehicula eu diam. Pellentesque rhoncus aliquam mattis. Ut vulputate eros sed felis sodales nec vulputate justo hendrerit. Vivamus varius pretium ligula, a aliquam odio euismod sit amet. Quisque laoreet sem sit amet orci ullamcorper at ultricies metus viverra. Pellentesque arcu mauris, malesuada quis ornare accumsan, blandit sed diam.</p>

<form class="abs register">
  <h2>REGISTER NOW</h2>
  <div class="field"><svg width="14" height="14" viewBox="0 0 14 14"><circle cx="7" cy="4" r="3.5" fill="#888"/><path d="M0 14a7 6 0 0 1 14 0z" fill="#888"/></svg>Name</div>
  <div class="field"><svg width="16" height="12" viewBox="0 0 16 12"><rect width="16" height="12" fill="#888"/><path d="M0 0l8 7 8-7" stroke="#fff" fill="none"/></svg>Email</div>
  <div class="field"><svg width="14" height="14" viewBox="0 0 14 14"><path d="M2 1l3 0 1 3-2 1a8 8 0 0 0 5 5l1-2 3 1v3a1 1 0 0 1-1 1A12 12 0 0 1 1 2a1 1 0 0 1 1-1z" fill="#888"/></svg>Contact number</div>
  <div class="field"><svg width="14" height="14" viewBox="0 0 14 14"><circle cx="7" cy="7" r="7" fill="#1a73d9"/><rect x="6" y="6" width="2" height="5" fill="#fff"/><circle cx="7" cy="4" r="1.1" fill="#fff"/></svg>Select Category<svg style="margin-left:14px" width="18" height="10" viewBox="0 0 18 10"><path d="M0 0h18L9 10z" fill="#777"/></svg></div>
  <div class="submit">SUBMIT</div>
</form>

<section class="abs grow">
  <h2>HOW VELTRANO HELP YOUR BUSINESS GROW</h2>
  <p class="intro">Lorem ipsum dolor sit amet, consectetur adipiscing elit. Nulla quam velit, vulputate eu pharetra nec, mattis ac neque. Duis vulputate commodo lectus, ac blandit elit tincidunt id. Sed rhoncus, tortor sed eleifend tristique, tortor mauris molestie elit, et lacinia ipsum quam nec dui. Quisque nec mauris sit amet elit iaculis pretium</p>
  <div class="feature" style="left:98px"><svg width="30" height="30" viewBox="0 0 30 30"><circle cx="15" cy="15" r="15" fill="#fff"/><text x="15" y="22" text-anchor="middle" font-family="Arimo,sans-serif" font-weight="700" font-size="20" fill="#878787">$</text></svg><h3>Money Back Guarantee</h3><p>Lorem ipsum dolor sit amet, consectetur adipiscing elit. Nulla quam velit, vulputate eu pharetra nec, mattis ac neque. Duis vulputate commodo lectus, ac</p></div>
  <div class="feature" style="left:274px"><svg width="54" height="34" viewBox="0 0 54 34" fill="none" stroke="#fff" stroke-width="1.5"><rect x="5" y="14" width="5" height="18"/><rect x="14" y="4" width="5" height="28"/><rect x="23" y="10" width="5" height="22"/><rect x="32" y="18" width="5" height="14"/><rect x="41" y="26" width="5" height="6"/><path d="M1 1v32h52"/></svg><h3 style="margin-top:2px">Virtual Balancing</h3><p>Lorem ipsum dolor sit amet, consectetur adipiscing elit. Nulla quam velit, vulputate eu pharetra nec, mattis ac neque. Duis vulputate commodo lectus, ac</p></div>
  <div class="feature" style="left:428px"><svg width="30" height="30" viewBox="0 0 30 30" fill="none" stroke="#fff" stroke-width="3"><circle cx="15" cy="15" r="13"/><path d="M15 7v8h6"/></svg><h3>Save Time</h3><p>Lorem ipsum dolor sit amet, consectetur adipiscing elit. Nulla quam velit, vulputate eu pharetra nec, mattis ac neque. Duis vulputate commodo lectus, ac</p></div>
  <div class="feature" style="left:589px"><svg width="34" height="34" viewBox="0 0 34 34"><rect x="1" y="4" width="32" height="30" rx="3" fill="#fff"/><rect x="12" y="0" width="10" height="6" rx="2" fill="#fff"/><circle cx="17" cy="15" r="5" fill="#878787"/><path d="M7 29a10 8 0 0 1 20 0z" fill="#878787"/></svg><h3 style="margin-top:2px">Timeline and Schedule</h3><p>Lorem ipsum dolor sit amet, consectetur adipiscing elit. Nulla quam velit, vulputate eu pharetra nec, mattis ac neque. Duis vulputate commodo lectus, ac</p></div>
</section>

<div class="abs services-photo" role="img" aria-label="Photo of an old town riverfront with church spires at dusk"></div>
<h2 class="abs services-title">OUR SERVICES</h2>
<p class="abs services-text">Lorem ipsum dolor sit amet, consectetur adipiscing elit. Nulla quam velit, vulputate eu pharetra nec, mattis ac neque. Duis vulputate commodo lectus, ac blandit elit tincidunt id. Sed rhoncus, tortor sed eleifend tristique, tortor mauris molestie elit, et lacinia ipsum quam nec dui. Quisque nec mauris sit amet elit iaculis pretium sit amet quis magna. Aenean velit odio, elementum in tempus ut, vehicula eu diam. Pellentesque rhoncus aliquam mattis. Ut vulputate eros sed felis sodales nec vulputate justo hendrerit. Vivamus varius pretium ligula, a aliquam odio euismod sit amet. Quisque laoreet sem sit amet orci ullamcorper at ultricies metus viverra. Pellentesque arcu mauris, malesuada quis ornare accumsan, blandit sed diam.</p>

<section class="abs team">
  <h2>OUR TEAM</h2>
  <p>Lorem ipsum dolor sit amet, consectetur adipiscing elit. Nulla quam velit, vulputate eu pharetra nec, mattis ac neque. Duis vulputate commodo lectus, ac blandit elit tincidunt id. Sed rhoncus, tortor sed eleifend tristique, tortor mauris molestie elit, et lacinia ipsum quam nec dui. Quisque nec mauris sit amet elit iaculis pretium sit amet quis magna. Aenean velit odio, elementum in tempus ut, vehicula eu diam. Pellentesque rhoncus aliquam mattis. Ut vulputate eros sed felis sodales nec vulputate justo hendrerit. Vivamus varius pretium ligula, a aliquam odio euismod sit amet. Quisque laoreet sem sit amet orci ullamcorper at ultricies metus viverra. Pellentesque arcu mauris, malesuada quis ornare accumsan, blandit sed diam.</p>
</section>
<div class="abs team-button">Register Now</div>

<h2 class="abs blog-title">OUR BLOG</h2>
<article class="abs post" style="left:63px"><div class="post-thumb" role="img" aria-label="Blog post image placeholder"><svg width="110" height="64" viewBox="0 0 110 64"><path d="M0 64L30 14q6-8 12 0l18 28 10-12q5-6 10 0l22 34z" fill="#bdbdbd"/><circle cx="92" cy="14" r="14" fill="#bdbdbd"/></svg></div><h3>Title Here 1</h3><p>Lorem ipsum dolor sit amet, consectetur adipiscing elit. Nulla quam velit, vulputate eu pharetra nec, mattis ac neque. Duis vulputate commodo lectus, ac blandit elit tincidunt id. Sed rhoncus, tortor sed eleifend tristique, tortor mauris molestie elit, et lacinia ipsum quam nec dui. Quisque nec mauris sit</p><a>Read More</a></article>
<article class="abs post" style="left:299px"><div class="post-thumb" role="img" aria-label="Blog post image placeholder"><svg width="110" height="64" viewBox="0 0 110 64"><path d="M0 64L30 14q6-8 12 0l18 28 10-12q5-6 10 0l22 34z" fill="#bdbdbd"/><circle cx="92" cy="14" r="14" fill="#bdbdbd"/></svg></div><h3>Title Here 1</h3><p>Lorem ipsum dolor sit amet, consectetur adipiscing elit. Nulla quam velit, vulputate eu pharetra nec, mattis ac neque. Duis vulputate commodo lectus, ac blandit elit tincidunt id. Sed rhoncus, tortor sed eleifend tristique, tortor mauris molestie elit, et lacinia ipsum quam nec dui. Quisque nec mauris sit</p><a>Read More</a></article>
<article class="abs post" style="left:536px"><div class="post-thumb" role="img" aria-label="Blog post image placeholder"><svg width="110" height="64" viewBox="0 0 110 64"><path d="M0 64L30 14q6-8 12 0l18 28 10-12q5-6 10 0l22 34z" fill="#bdbdbd"/><circle cx="92" cy="14" r="14" fill="#bdbdbd"/></svg></div><h3>Title Here 1</h3><p>Lorem ipsum dolor sit amet, consectetur adipiscing elit. Nulla quam velit, vulputate eu pharetra nec, mattis ac neque. Duis vulputate commodo lectus, ac blandit elit tincidunt id. Sed rhoncus, tortor sed eleifend tristique, tortor mauris molestie elit, et lacinia ipsum quam nec dui. Quisque nec mauris sit</p><a>Read More</a></article>

<footer class="abs site-footer">
  <p class="footer-links">About us | Privacy Policy | Terms and Conditions | Sponsors | FAQ</p>
  <div class="socials">
    <span class="social" style="background:#2d5fa8" aria-label="Social profile link"></span>
    <span class="social" style="background:#1b86b8" aria-label="Social profile link"></span>
    <span class="social" style="background:#d42a22" aria-label="Social profile link"></span>
  </div>
</footer>
</body>
</html>
```